BHSC Business cards

We are an established dental practice that is looking for new business cards to match our new logo. We are looking for something unique and sophisticated.
BRIEF: Colours are black, silver and white. Include the company name, logo (including “Pelwick Heath Dental Care”) and phone number “03 9415 2876”.
Front - Include the company name, logo (including “Pelwick Heath Dental Care”) and phone number “03 9415 2876”.
Back - Include the company name,  “Pelwick Heath Dental Care”, phone number “03 9415 2876”. address "64A Tindle Street, Pelwick Heath, Vic 3187", "Email reception@pelwickheathdentalcare.com.au", the Dentist Name " Dr ................................"  Your next appointment "Day, date and time(am/pm)".  3 lines for 3 appointments please, and at the bottom "IF UNABLE TO KEEP THIS APPOINTMENT 48 HOURS NOTICE IS REQUIRED."
Try and be creative and different with the design, i've added an image for inspiration

Target Market(s)
ALL in need of dental
Industry/Entity Type
Dental Clinic
Look and feel
Each slider illustrates characteristics of the customer's brand and the style your logo design should communicate.

```html
<!DOCTYPE html>
<html lang="en">
<head>
<meta charset="utf-8">
<title>Pelwick Heath Dental Care – Business Cards</title>
<link href="https://fonts.googleapis.com/css2?family=Roboto:ital,wght@0,400;0,700;0,900;1,400&display=swap" rel="stylesheet">
<style>
  :root{
    --bg:#3a3a3a;
    --card:#141414;
    --silver:#cfcfcf;
    --silver-dim:#8f8f8f;
    --white:#ffffff;
    --ink:#1a1a1a;
  }
  *{box-sizing:border-box;margin:0;padding:0}
  html,body{width:799px;height:1200px;overflow:hidden}
  body{background:var(--bg);font-family:"Roboto",Arial,sans-serif;position:relative}
  .card{position:absolute;left:50px;width:700px;height:400px;background:var(--card);border-radius:6px;overflow:hidden;box-shadow:0 12px 30px rgba(0,0,0,.45)}
  .card--appointment{top:140px}
  .card--contact{top:660px}

  /* brand lockup */
  .brand{position:absolute;display:flex;align-items:center;gap:14px}
  .brand__mark{width:44px;height:44px;border-radius:50%;background:var(--silver-dim)}
  .brand__name{font-weight:900;color:var(--silver);font-size:30px;letter-spacing:1px;line-height:1}
  .brand__sub{font-weight:900;color:var(--silver);font-size:13px;letter-spacing:3px;margin-top:4px}
  .card--appointment .brand{top:18px;left:150px}
  .rule{position:absolute;height:1px;background:var(--silver-dim)}

  /* appointment panel */
  .panel{position:absolute;left:22px;top:96px;width:656px;height:206px;background:var(--white);border-radius:20px;padding:38px 26px 0 22px}
  .tag{position:absolute;right:40px;top:84px;background:var(--card);color:var(--white);border:2px solid var(--white);border-radius:8px;padding:5px 16px;font-weight:700;font-size:14px;letter-spacing:.5px}
  .slot{display:flex;align-items:flex-end;font-size:17px;color:var(--ink);height:52px}
  .slot__fill{flex:1;border-bottom:2px dotted #555;margin:0 6px 5px}
  .slot__fill--date{flex:1.1}
  .footer-row{position:absolute;left:22px;top:318px;display:flex;gap:26px;color:var(--white);font-size:14px;align-items:center}
  .footer-row span{display:flex;align-items:center;gap:7px}
  .notice{position:absolute;left:22px;right:22px;top:352px;color:var(--white);font-weight:700;font-size:17px;letter-spacing:.3px}
  svg.icon{width:15px;height:15px;fill:var(--white)}

  /* contact side */
  .seal{position:absolute;left:-90px;top:20px;width:360px;height:360px;border-radius:50%;background:var(--silver)}
  .card--contact .brand{right:40px;top:40px;text-align:right}
  .card--contact .brand__name{font-size:34px}
  .card--contact .brand__sub{font-size:15px;letter-spacing:5px}
  .dentist{position:absolute;right:40px;top:138px;text-align:right;color:var(--silver)}
  .dentist__name{font-weight:900;font-size:24px}
  .dentist__role{font-style:italic;font-size:16px;margin-top:3px}
  .details{position:absolute;right:40px;top:210px;text-align:right;color:var(--silver);font-size:16px;line-height:1.5}
  .details__address{margin-bottom:14px}
  .details li{list-style:none;display:flex;justify-content:flex-end;align-items:center;gap:10px}
  .details svg.icon{fill:var(--silver)}
</style>
</head>
<body>

<section class="card card--appointment" aria-label="Appointment card">
  <div class="rule" style="left:22px;top:60px;width:120px"></div>
  <div class="rule" style="right:22px;top:60px;width:60px"></div>
  <div class="brand">
    <div class="brand__mark"></div>
    <div>
      <div class="brand__name">PELWICK HEATH</div>
      <div class="brand__sub">DENTAL CARE — 03 9415 2876</div>
    </div>
  </div>

  <div class="panel">
    <div class="slot">Date<span class="slot__fill slot__fill--date"></span>at<span class="slot__fill"></span>am / pm</div>
    <div class="slot">Date<span class="slot__fill slot__fill--date"></span>at<span class="slot__fill"></span>am / pm</div>
    <div class="slot">Date<span class="slot__fill slot__fill--date"></span>at<span class="slot__fill"></span>am / pm</div>
  </div>
  <div class="tag">YOUR NEXT APPOINTMENT</div>

  <div class="footer-row">
    <span><svg class="icon" viewBox="0 0 24 24"><path d="M2 5h20v14H2z M3 6l9 7 9-7" fill="none" stroke="#fff" stroke-width="2"/></svg>reception@pelwickheathdentalcare.com.au</span>
    <span><svg class="icon" viewBox="0 0 24 24"><path d="M12 2a7 7 0 0 0-7 7c0 5 7 13 7 13s7-8 7-13a7 7 0 0 0-7-7zm0 10a3 3 0 1 1 0-6 3 3 0 0 1 0 6z"/></svg>64A Tindle Street, Pelwick Heath, Vic 3187</span>
  </div>
  <p class="notice">IF UNABLE TO KEEP THIS APPOINTMENT 48 HOURS NOTICE IS REQUIRED</p>
</section>

<section class="card card--contact" aria-label="Contact card">
  <div class="seal"></div>
  <div class="brand">
    <div>
      <div class="brand__name">PELWICK HEATH</div>
      <div class="brand__sub">DENTAL CARE</div>
    </div>
  </div>
  <div class="dentist">
    <div class="dentist__name">Dr. Alden Marsh</div>
    <div class="dentist__role">Senior Dentist</div>
  </div>
  <div class="details">
    <div class="details__address">64A Tindle Street,<br>Pelwick Heath, Vic 3187</div>
    <ul>
      <li>03 9415 2876<svg class="icon" viewBox="0 0 24 24"><path d="M6.6 10.8a15 15 0 0 0 6.6 6.6l2.2-2.2a1 1 0 0 1 1-.25 11.4 11.4 0 0 0 3.6.57 1 1 0 0 1 1 1V20a1 1 0 0 1-1 1A17 17 0 0 1 3 4a1 1 0 0 1 1-1h3.5a1 1 0 0 1 1 1c0 1.25.2 2.45.57 3.57a1 1 0 0 1-.25 1z"/></svg></li>
      <li>www.pelwickheathdentalcare.com.au<svg class="icon" viewBox="0 0 24 24"><circle cx="12" cy="12" r="9" fill="none" stroke="#cfcfcf" stroke-width="2"/><path d="M3 12h18M12 3c3 3 3 15 0 18M12 3c-3 3-3 15 0 18" fill="none" stroke="#cfcfcf" stroke-width="1.5"/></svg></li>
      <li>reception@pelwickheathdentalcare.com.au<svg class="icon" viewBox="0 0 24 24"><path d="M2 5h20v14H2z M3 6l9 7 9-7" fill="none" stroke="#cfcfcf" stroke-width="2"/></svg></li>
    </ul>
  </div>
</section>

</body>
</html>
```